Post Lockdown Ortho Special

We are running a special for (Ortho) Braces/Clear Aligner (Quorventa), till July 31st 2020. Up to $2,000 off with free Consultation and Xrays.

We need a ad to run in different formats.

Maybe something with: what better time to get braces when you have to wear a mask all the time.

Trying to rebuild our business and get people in for free consultations.

```html
<!DOCTYPE html>
<html lang="en">
<head>
<meta charset="utf-8">
<title>Larchmont Family Dentistry – Post Lockdown Ortho Special</title>
<link href="https://fonts.googleapis.com/css2?family=Montserrat:wght@800;900&family=Nunito:wght@600;700;800&display=swap" rel="stylesheet">
<style>
  :root {
    --purple: #6a46a0;
    --olive: #a3a04f;
    --olive-text: #9d9a44;
    --lavender: #dcd3e9;
    --beige: #e6e3cd;
    --white: #ffffff;
  }
  * { margin: 0; padding: 0; box-sizing: border-box; }
  html, body { width: 848px; height: 1200px; overflow: hidden; background: var(--white); }
  .flyer {
    position: relative; width: 848px; height: 1200px; overflow: hidden;
    background: var(--white); font-family: "Nunito", sans-serif; color: var(--purple);
  }
  .layer { position: absolute; left: 0; top: 0; }

  .brand { position: absolute; left: 51px; top: 54px; display: flex; align-items: center; gap: 14px; }
  .brand-mark { width: 84px; height: 84px; border-radius: 50%; background: var(--purple); flex: none; }
  .brand-name { font-weight: 800; color: var(--purple); }
  .brand-name .name { display: block; font-size: 26px; line-height: 28px; letter-spacing: 1px; }
  .brand-name .sub { display: block; font-size: 10px; line-height: 14px; letter-spacing: 3.2px; }

  .headline {
    position: absolute; left: 49px; top: 206px;
    font-family: "Montserrat", sans-serif; font-weight: 900; font-size: 60px; line-height: 66px;
    color: var(--white); letter-spacing: 0;
  }
  .headline .accent { color: var(--purple); }
  .tagline { position: absolute; left: 52px; top: 480px; font-weight: 700; font-size: 15.5px; line-height: 21px; color: var(--white); }

  .offer {
    position: absolute; left: 543px; top: 438px; width: 254px; height: 254px; border-radius: 50%;
    background: var(--purple); border: 3px solid var(--olive); color: var(--white);
    text-align: center; font-family: "Montserrat", sans-serif; font-weight: 900;
    display: flex; flex-direction: column; justify-content: center; padding-top: 4px;
  }
  .offer-line { font-size: 45px; line-height: 51px; }
  .offer-date { font-family: "Nunito", sans-serif; font-weight: 800; font-size: 16px; margin-top: 6px; }

  .section-tag {
    position: absolute; left: 0; top: 622px; height: 46px; width: 335px;
    background: var(--purple); clip-path: polygon(0 0, 305px 0, 100% 100%, 0 100%);
    color: var(--white); font-weight: 800; font-size: 23px; line-height: 46px; padding-left: 51px;
  }

  .service { position: absolute; display: flex; gap: 18px; align-items: flex-start; }
  .service-icon { width: 59px; height: 59px; border-radius: 50%; flex: none; margin-top: 3px; }
  .service-icon.olive { background: var(--olive); }
  .service-icon.purple { background: var(--purple); }
  .service-title { font-weight: 700; font-size: 22px; line-height: 26px; color: var(--olive-text); }
  .service-text { font-weight: 700; font-size: 15.5px; line-height: 21px; color: var(--purple); }

  .mask-note { position: absolute; left: 51px; top: 914px; font-weight: 700; font-size: 21px; line-height: 26px; color: var(--olive-text); }
  .mask-note::after { content: ""; display: block; width: 77px; height: 1.5px; background: var(--purple); margin-top: 8px; }
  .about { position: absolute; left: 427px; top: 908px; width: 355px; font-weight: 600; font-size: 15.5px; line-height: 20.5px; color: var(--purple); }

  .divider { position: absolute; left: 0; top: 1026px; width: 848px; height: 1px; background: var(--purple); }
  .site-pill {
    position: absolute; left: 270px; top: 1007px; width: 308px; height: 39px; border-radius: 20px;
    background: var(--purple); color: var(--white); text-align: center;
    font-weight: 800; font-size: 19.5px; line-height: 39px; letter-spacing: 0.3px;
  }

  .hotline-icon { position: absolute; left: 53px; top: 1074px; width: 34px; height: 34px; border-radius: 50%; background: var(--purple); }
  .hotline-label { position: absolute; left: 100px; top: 1072px; font-weight: 700; font-size: 22px; color: var(--olive-text); }
  .hotline-number { position: absolute; left: 100px; top: 1102px; font-family: "Montserrat", sans-serif; font-weight: 800; font-size: 34px; color: var(--purple); }

  .contact { position: absolute; left: 425px; display: flex; align-items: center; gap: 13px; font-weight: 600; font-size: 15.5px; line-height: 19px; color: var(--purple); }
  .contact-icon { width: 21px; height: 21px; border-radius: 50%; background: var(--olive); flex: none; }
</style>
</head>
<body>
<div class="flyer">

  <svg class="layer" width="848" height="1200" viewBox="0 0 848 1200" aria-hidden="true">
    <rect x="0" y="670" width="848" height="530" fill="var(--lavender)"/>
    <polygon points="0,670 848,670 424,935" fill="var(--beige)"/>
    <polygon points="0,1200 848,1200 424,935" fill="var(--beige)"/>
  </svg>

  <svg class="layer" width="848" height="700" viewBox="0 0 848 700" role="img" aria-label="Photo of three smiling dental team members in white coats and scrubs">
    <defs>
      <radialGradient id="photoTone" cx="0.5" cy="0.45" r="0.6">
        <stop offset="0" stop-color="#f3f2f4"/>
        <stop offset="1" stop-color="#dcdbe0"/>
      </radialGradient>
    </defs>
    <circle cx="578" cy="313" r="260" fill="url(#photoTone)"/>
  </svg>

  <svg class="layer" width="848" height="700" viewBox="0 0 848 700" aria-hidden="true">
    <circle cx="166" cy="374" r="221" fill="var(--olive)" opacity="0.94"/>
  </svg>

  <div class="brand">
    <div class="brand-mark"></div>
    <div class="brand-name">
      <span class="name">LARCHMONT</span>
      <span class="sub">FAMILY DENTISTRY</span>
      <span class="sub">DR MAREN ELLWOOD</span>
    </div>
  </div>

  <h1 class="headline">
    <span class="accent">YOUR</span><br>
    SMILE<br>
    <span class="accent">IS</span> OUR<br>
    <span class="accent">PRIORITY</span>
  </h1>
  <p class="tagline">Braces and clear aligners for<br>you and your family...</p>

  <div class="offer">
    <div class="offer-line">UP TO</div>
    <div class="offer-line">$2,000</div>
    <div class="offer-line">OFF</div>
    <div class="offer-date">till july 31st,2020</div>
  </div>

  <div class="section-tag">Ortho Services</div>

  <div class="service" style="left:51px; top:704px;">
    <svg class="service-icon olive" viewBox="0 0 59 59" aria-hidden="true">
      <g fill="none" stroke="#fff" stroke-width="1.8" stroke-linejoin="round">
        <path d="M17 20 q12 -6 25 0 v6 q-12 4 -25 0 Z"/><path d="M17 33 q12 -4 25 0 v6 q-12 6 -25 0 Z"/>
        <path d="M14 23 h31 M14 36 h31"/>
      </g>
    </svg>
    <div><div class="service-title">Braces</div><div class="service-text">Straighter smiles with metal<br>or ceramic braces...</div></div>
  </div>

  <div class="service" style="left:425px; top:704px;">
    <svg class="service-icon purple" viewBox="0 0 59 59" aria-hidden="true">
      <g fill="none" stroke="#fff" stroke-width="1.8" stroke-linejoin="round">
        <rect x="28" y="14" width="14" height="9" rx="1"/><circle cx="24" cy="27" r="3.5"/>
        <path d="M17 42 v-7 a7 7 0 0 1 14 0 v7"/><path d="M14 42 h30 M36 42 v-8 h6 v8"/>
      </g>
    </svg>
    <div><div class="service-title">Free Consultation</div><div class="service-text">Meet our ortho team and<br>plan your new smile...</div></div>
  </div>

  <div class="service" style="left:51px; top:794px;">
    <svg class="service-icon purple" viewBox="0 0 59 59" aria-hidden="true">
      <path d="M18 20 q11 -6 23 0 q2 9 -3 22 h-4 l-2 -8 h-5 l-2 8 h-4 q-5 -13 -3 -22 Z" fill="none" stroke="#fff" stroke-width="1.8" stroke-linejoin="round"/>
    </svg>
    <div><div class="service-title">Quorventa Aligners</div><div class="service-text">Clear aligners that fit into<br>your daily routine...</div></div>
  </div>

  <div class="service" style="left:425px; top:794px;">
    <svg class="service-icon olive" viewBox="0 0 59 59" aria-hidden="true">
      <g fill="none" stroke="#fff" stroke-width="1.8" stroke-linejoin="round">
        <rect x="16" y="16" width="27" height="27" rx="2"/><path d="M22 37 l5 -8 4 5 3 -4 4 7"/><circle cx="24" cy="23" r="2"/>
      </g>
    </svg>
    <div><div class="service-title">Free X-rays</div><div class="service-text">Digital X-rays included with<br>every consultation...</div></div>
  </div>

  <p class="mask-note">Wearing a mask all day? What<br>better time to get braces...</p>
  <p class="about">Post lockdown ortho special: up to $2,000 off braces or Quorventa clear aligners, with a free consultation and X-rays.</p>

  <div class="divider"></div>
  <div class="site-pill">www.yoursitename.com</div>

  <svg class="hotline-icon" viewBox="0 0 34 34" aria-hidden="true">
    <path d="M12 9 l3 4 -2 2 a10 10 0 0 0 6 6 l2 -2 4 3 -2 3 a13 13 0 0 1 -14 -14 z" fill="none" stroke="#fff" stroke-width="1.5"/>
  </svg>
  <div class="hotline-label">Free Ortho Consultation</div>
  <div class="hotline-number">0123-456-789</div>

  <div class="contact" style="top:1059px;">
    <svg class="contact-icon" viewBox="0 0 21 21" aria-hidden="true"><path d="M7 5 l2 3 -1.5 1.5 a7 7 0 0 0 4 4 l1.5 -1.5 3 2 -1.5 2 a9 9 0 0 1 -9.5 -9.5 z" fill="none" stroke="#fff" stroke-width="1.3"/></svg>
    <span>123 456 789<br>245 456 789</span>
  </div>
  <div class="contact" style="top:1097px;">
    <svg class="contact-icon" viewBox="0 0 21 21" aria-hidden="true"><rect x="5" y="6.5" width="11" height="8" fill="none" stroke="#fff" stroke-width="1.3"/><path d="M5 6.5 l5.5 4.5 5.5 -4.5" fill="none" stroke="#fff" stroke-width="1.3"/></svg>
    <span>yourmail&amp;gmail.com</span>
  </div>
  <div class="contact" style="top:1125px;">
    <svg class="contact-icon" viewBox="0 0 21 21" aria-hidden="true"><path d="M5 10 l5.5 -5 5.5 5 M7 9 v6 h7 v-6" fill="none" stroke="#fff" stroke-width="1.3"/></svg>
    <span>yourlocation like 65 street Road like Australia</span>
  </div>

</div>
</body>
</html>
```